Brambleton Home Services Web Site

Design Web site with 3-4 pages: Home, About Us, Services and Order form / Schedule Appointment (which will likely be link to Quorvel App and Tallyfarn integration.)
Services include: Dryer Vent Cleaning, AC Cleaning, Difficult-to-Reach Light Bulb replacement, Wood Repair and Home Maintenance Plans including Fire Safety Checks and Filter Replacement.

Target Market(s)

Luxury Home Owners, Professionals (Dr's/lawyers) and Seniors

Industry/Entity Type

Home Maintenance

Coding

Coded - Design and coding required

Requirements
Must have
• Tagline - Where Home Maintenance is Effortless

```html
<!DOCTYPE html>
<html lang="en">
<head>
<meta charset="utf-8">
<title>Brambleton Home Services</title>
<link href="https://fonts.googleapis.com/css2?family=Montserrat:wght@500;600;700&family=Figtree:wght@400;500;600&display=swap" rel="stylesheet">
<style>
:root{
  --gold:#e0a82e;
  --gold-dark:#c98f17;
  --ink:#1a1a1a;
  --text:#3a3a3a;
  --muted:#8a8a8a;
  --cream:#fdf6e8;
  --white:#ffffff;
  --black:#000000;
}
*{margin:0;padding:0;box-sizing:border-box}
html,body{width:1200px;height:3694px;overflow:hidden}
body{position:relative;font-family:'Figtree',sans-serif;color:var(--text);background:var(--white)}
.abs{position:absolute}
.heading{font-family:'Montserrat',sans-serif;font-weight:600;color:var(--gold);font-size:44px;letter-spacing:.5px;text-transform:uppercase;white-space:nowrap}
.kicker{font-family:'Montserrat',sans-serif;font-size:16px;letter-spacing:4px;color:var(--ink);display:flex;align-items:center;gap:14px;text-transform:uppercase}
.kicker::before,.kicker::after{content:"";width:40px;height:2px;background:var(--ink)}
.dot{display:inline-block;width:30px;height:30px;border-radius:50%;border:2px solid var(--gold);flex:none}
.btn{display:inline-flex;align-items:center;justify-content:center;background:var(--gold);color:var(--white);font-family:'Montserrat',sans-serif;font-weight:700;border-radius:30px;text-transform:uppercase}

/* header */
.header{top:0;left:0;width:1200px;height:117px;background:var(--white)}
.brand-box{left:106px;top:0;width:192px;height:156px;background:var(--white);z-index:5;display:flex;flex-direction:column;align-items:center;justify-content:flex-end;padding-bottom:22px;box-shadow:0 4px 10px rgba(0,0,0,.08)}
.brand-box .dot{margin-bottom:12px}
.brand-name{font-family:'Montserrat',sans-serif;font-weight:700;color:var(--gold);font-size:22px;letter-spacing:2px}
.brand-sub{font-size:12px;color:var(--muted);letter-spacing:1px;margin-top:2px}
.phone{left:632px;top:22px;display:flex;align-items:center;gap:10px;font-family:'Montserrat',sans-serif;font-weight:600;color:var(--gold);font-size:18px}
.phone-ic{width:32px;height:32px;border-radius:50%;background:#555;display:flex;align-items:center;justify-content:center}
.header .btn{left:843px;top:14px;width:252px;height:46px;font-size:15px}
.nav{top:80px;left:408px;display:flex;gap:44px;font-family:'Montserrat',sans-serif;font-weight:600;font-size:15px;color:var(--ink)}
.nav .active{color:var(--gold);position:relative}
.nav .active::after{content:"";position:absolute;left:-8px;right:-8px;top:28px;height:6px;background:var(--gold)}

/* hero */
.hero{top:117px;left:0;width:1200px;height:680px;overflow:hidden}
.hero-photo{position:absolute;inset:0;background:linear-gradient(90deg,#3c3f44 0%,#6d7075 45%,#8a8f92 60%,#2f4c7d 80%,#5d7a5b 100%)}
.hero-shade{position:absolute;inset:0;background:linear-gradient(90deg,rgba(0,0,0,.55),rgba(0,0,0,.1) 60%,transparent)}
.hero h1{position:absolute;left:105px;top:130px;font-family:'Montserrat',sans-serif;font-weight:600;color:var(--white);font-size:46px;line-height:59px;text-transform:uppercase}
.hero p{position:absolute;left:106px;top:318px;color:var(--white);font-size:17px;line-height:31px;width:580px}
.hero .btn{position:absolute;left:106px;top:402px;width:264px;height:52px;font-size:15px;color:var(--ink)}
.hero svg{position:absolute;left:0;top:0}

/* about */
.about-bg{top:780px;left:0;width:1200px;height:520px}
.about-art{left:34px;top:880px;width:570px;height:335px;border-radius:14px;background:linear-gradient(135deg,#8a6a30,#d8a93a 55%,#a57a28)}
.about-text{left:645px;top:875px;width:520px}
.about-text .heading{display:flex;align-items:center;gap:12px;font-size:38px}
.about-text .kicker{margin-top:8px;font-size:15px}
.about-lead{color:var(--gold);font-weight:600;font-size:18px;margin-top:14px}
.about-body{font-size:14px;line-height:26px;margin-top:10px;width:440px}
.about-text .btn{margin-top:26px;width:160px;height:50px;font-size:17px}

/* services */
.svc-title{top:1345px;left:0;width:1200px;text-align:center}
.svc-title .heading{display:inline-flex;align-items:center;gap:12px}
.svc-title .kicker{justify-content:center;margin-top:6px}
.card{top:1470px;background:var(--white);box-shadow:0 4px 16px rgba(0,0,0,.1);height:395px;text-align:center;padding:16px 12px 0}
.card-img{height:200px}
.card h3{font-family:'Montserrat',sans-serif;font-weight:600;font-size:19px;color:var(--ink);margin-top:24px}
.card p{font-size:16px;line-height:28px;margin-top:8px;color:var(--text)}
.card a{display:block;color:var(--muted);font-size:14px;margin-top:8px;text-decoration:underline}
.arrow{top:1650px;width:36px;height:36px;border-radius:50%;display:flex;align-items:center;justify-content:center}

/* contact band */
.contact{top:1955px;left:0;width:1200px;height:510px;overflow:hidden}
.contact-photo{position:absolute;inset:0;background:linear-gradient(110deg,#4a4a4a,#6b6358 50%,#8a6a3a 80%,#5a5550)}
.contact-shade{position:absolute;inset:0;background:rgba(40,40,40,.55)}
.contact svg{position:absolute;left:0;top:0}
.contact-inner{position:absolute;top:75px;left:0;width:1200px;text-align:center;color:var(--white)}
.contact-inner .heading{color:var(--white);display:inline-flex;align-items:center;gap:12px}
.contact-inner .dot{border-color:var(--white)}
.contact-inner .kicker{color:var(--white);justify-content:center;margin-top:6px}
.contact-inner .kicker::before,.contact-inner .kicker::after{background:var(--white)}
.contact-inner p{font-size:15px;line-height:26px;width:760px;margin:40px auto 0}
.contact-inner .btn{margin-top:42px;background:var(--white);color:var(--gold);width:280px;height:52px;font-size:16px}

/* testimonials */
.tst-title{top:2540px;left:0;width:1200px;text-align:center}
.tst-title .heading{display:inline-flex;align-items:center;gap:12px}
.tst-title .kicker{justify-content:center;margin-top:6px}
.tst{top:2690px;font-size:16px;line-height:28px}
.stars{color:var(--gold);font-size:18px;letter-spacing:1px}
.tst p{margin-top:14px}
.who{display:flex;align-items:center;gap:12px;margin-top:18px}
.avatar{width:64px;height:64px;border-radius:50%;background:linear-gradient(135deg,#bfb3a3,#6d6155)}
.who b{display:block;font-size:14px;color:var(--ink);font-weight:600}
.who span{font-size:13px;color:var(--muted)}
.tst.active{border:1px solid var(--gold);padding:22px 16px;background:var(--white)}
.clip{left:0;top:2680px;width:1200px;height:400px;overflow:hidden}

/* footer */
.footer{top:3110px;left:0;width:1200px;height:584px}
.footer svg{position:absolute;left:0;top:0}
.f-brand{left:92px;top:3320px;width:315px;text-align:center;color:var(--white)}
.f-brand .dot{width:60px;height:60px;border-width:3px}
.f-brand .brand-name{font-size:34px;margin-top:16px;letter-spacing:3px}
.f-brand .brand-sub{color:var(--white);font-size:18px;letter-spacing:2px;display:flex;align-items:center;gap:10px;justify-content:center}
.f-brand .brand-sub::before,.f-brand .brand-sub::after{content:"";width:40px;height:1px;background:var(--white)}
.tagline{font-size:14px;color:var(--gold);margin-top:10px;font-style:normal;letter-spacing:.3px}
.f-col{top:3345px;color:var(--white)}
.f-col h4{font-family:'Montserrat',sans-serif;font-weight:500;font-size:20px}
.f-col ul{list-style:none;margin-top:16px}
.f-col li{font-size:15px;line-height:35px;display:flex;align-items:center;gap:8px}
.f-col li::before{content:"➔";font-size:12px;color:#bbb}
.f-contact{top:3345px;left:858px;color:var(--white)}
.f-contact h4{font-family:'Montserrat',sans-serif;font-weight:500;font-size:20px}
.c-row{display:flex;gap:12px;font-size:15px;line-height:27px;margin-top:16px;align-items:flex-start}
.c-ic{width:32px;height:32px;border-radius:50%;background:var(--white);flex:none;display:flex;align-items:center;justify-content:center}
.rule{left:103px;top:3590px;width:987px;height:1px;background:#888}
.copy{top:3626px;left:0;width:1200px;text-align:center;color:var(--white);font-size:15px}
</style>
</head>
<body>

<header class="abs header">
  <div class="abs brand-box">
    <span class="dot"></span>
    <div class="brand-name">BRAMBLETON</div>
    <div class="brand-sub">HOME SERVICES</div>
  </div>
  <div class="abs phone"><span class="phone-ic"><svg width="16" height="16" viewBox="0 0 24 24"><path fill="#fff" d="M6.6 10.8a15 15 0 0 0 6.6 6.6l2.2-2.2c.3-.3.7-.4 1-.2 1.1.4 2.3.6 3.6.6.6 0 1 .4 1 1V20c0 .6-.4 1-1 1A17 17 0 0 1 3 4c0-.6.4-1 1-1h3.5c.6 0 1 .4 1 1 0 1.3.2 2.5.6 3.6.1.3 0 .7-.2 1z"/></svg></span>+1-555-014-2290</div>
  <span class="abs btn">Schedule Appointment</span>
  <nav class="abs nav">
    <span class="active">HOME</span><span>ABOUT US</span><span>SERVICES</span><span>TESTIMONIALS</span><span>BLOG</span><span>CONTACT US</span>
  </nav>
</header>

<section class="abs hero">
  <div class="hero-photo" role="img" aria-label="Smiling home maintenance technician in a navy uniform holding a clipboard in front of a house"></div>
  <div class="hero-shade"></div>
  <h1>Smart solutions<br>for every corner of<br>your home</h1>
  <p>Reliable home maintenance services designed to keep your home safe, efficient, and worry-free.</p>
  <span class="btn">Schedule Appointment</span>
  <svg width="1200" height="680" viewBox="0 0 1200 680">
    <polygon points="0,498 600,660 1200,508 1200,680 0,680" fill="#e0a82e"/>
    <polygon points="0,530 600,690 1200,540 1200,680 0,680" fill="#fff"/>
    <circle cx="600" cy="648" r="44" fill="#fff"/>
    <circle cx="600" cy="648" r="14" fill="none" stroke="#e0a82e" stroke-width="2"/>
    <circle cx="582" cy="561" r="4" fill="#fff" opacity=".6"/><circle cx="600" cy="561" r="4" fill="#fff"/><circle cx="618" cy="561" r="4" fill="#fff" opacity=".6"/>
  </svg>
</section>

<svg class="abs about-bg" width="1200" height="520" viewBox="0 0 1200 520"><polygon points="640,20 1200,20 1200,520 1010,520" fill="#fdf6e8"/></svg>
<div class="abs about-art" role="img" aria-label="Decorative golden artwork with home photography"></div>
<div class="abs about-text">
  <h2 class="heading"><span class="dot"></span>About Brambleton</h2>
  <div class="kicker">Home Services</div>
  <div class="about-lead">We have over 20 years' experience</div>
  <p class="about-body">Lorem ipsum dolor sit amet, consectetur adipiscing elit, sed do eiusmod tempor incididunt ut labore et dolore magna aliqua. Ut ullamco laboris nisi ut aliquip ex ea commodo consequat.</p>
  <p class="about-body" style="margin-top:26px">Duis aute irure dolor in reprehenderit in voluptate velit esse cillum dolore eu fugiat nulla pariatur.</p>
  <span class="btn">Read More</span>
</div>

<div class="abs svc-title">
  <h2 class="heading"><span class="dot"></span>Our Services</h2>
  <div class="kicker">We Offer</div>
</div>
<span class="abs arrow" style="left:35px;background:#ccc"><svg width="18" height="18" viewBox="0 0 24 24"><path d="M20 11H7l5-5-1.4-1.4L3.2 12l7.4 7.4L12 18l-5-5h13z" fill="#fff"/></svg></span>
<span class="abs arrow" style="left:1130px;background:#555"><svg width="18" height="18" viewBox="0 0 24 24"><path d="M4 11h13l-5-5 1.4-1.4 7.4 7.4-7.4 7.4L12 18l5-5H4z" fill="#fff"/></svg></span>

<article class="abs card" style="left:107px;width:296px;border-top-left-radius:110px">
  <div class="card-img" role="img" aria-label="Row of commercial dryers with folded towels" style="background:linear-gradient(135deg,#6d7278,#c9ccd0 60%,#e8e8e8);border-top-left-radius:100px"></div>
  <h3>DRYER VENT CLEANING</h3>
  <p>Excepteur sint occaecat cupidatat non proident, sunt in culpa qui officiaan</p>
  <a>Read More</a>
</article>
<article class="abs card" style="left:450px;width:285px">
  <div class="card-img" role="img" aria-label="Technician cleaning a wall-mounted air conditioner" style="background:linear-gradient(135deg,#eef0f2,#cfd4d8 55%,#4b5f8a)"></div>
  <h3>AC CLEANING</h3>
  <p>Excepteur sint occaecat cupidatat non proident, sunt in culpa qui officiaan</p>
  <a>Read More</a>
</article>
<article class="abs card" style="left:795px;width:297px;border-top-right-radius:110px">
  <div class="card-img" role="img" aria-label="Gloved hand repairing a wooden window frame" style="background:linear-gradient(135deg,#7a5a30,#d8b27a 55%,#b8bcc0);border-top-right-radius:100px"></div>
  <h3>WOOD REPAIR</h3>
  <p>Excepteur sint occaecat cupidatat non proident, sunt in culpa qui officiaan</p>
  <a>Read More</a>
</article>

<section class="abs contact">
  <div class="contact-photo" role="img" aria-label="Technician in a hard hat working on a ceiling fixture"></div>
  <div class="contact-shade"></div>
  <svg width="1200" height="510" viewBox="0 0 1200 510">
    <polygon points="0,330 600,460 1200,320 1200,510 0,510" fill="#e0a82e"/>
    <polygon points="0,420 600,505 1200,420 1200,510 0,510" fill="#fff"/>
  </svg>
  <div class="contact-inner">
    <h2 class="heading"><span class="dot"></span>Get in touch with us</h2>
    <div class="kicker">Contact Us</div>
    <p>Lorem ipsum dolor sit amet, consectetur adipiscing elit, sed do eiusmod tempor incididunt ut labore et dolore magna aliqua. Ut enim ad minim veniam, quis nostrud exercitation ullamco laboris nisi ut aliquip ex ea commodo consequat. Duis aute irure dolor in reprehenderit in voluptate velit esse cillum dolore eu fugiat nulla pariatur.</p>
    <span class="btn">Schedule Appointment</span>
  </div>
</section>

<div class="abs tst-title">
  <h2 class="heading"><span class="dot"></span>What our customer says</h2>
  <div class="kicker">Testimonials</div>
</div>
<div class="abs clip">
  <div class="abs tst" style="left:58px;top:10px;width:260px">
    <div class="stars">★★★★★</div>
    <p>Temporibus autem quibusdam et aut officiis debitis aut rerum neus saepe facere mus, onis voluptas eveniet ut et voluptates repudae sint et molestiae non lorem recusadae.</p>
    <div class="who"><span class="avatar"></span><div><b>Owen Halbrook</b><span>United States</span></div></div>
  </div>
  <div class="abs tst active" style="left:384px;top:13px;width:311px;height:352px">
    <div class="stars">★★★★★</div>
    <p>Itaque earum rerum hic tenetur a sapiene delectus, ut aut reicieis volupatibus maiores alias conse uatur aut perferndis doloribus asperiores reiciendis voluptatbus repellat</p>
    <div class="who"><span class="avatar"></span><div><b>TALIA</b><span>United States</span></div></div>
  </div>
  <div class="abs tst" style="left:740px;top:10px;width:280px">
    <div class="stars">★★★★★</div>
    <p>At vero eos et accusamus et iusto odio dignissimos ducimus qui blaiis praesentium voluptatum deleniti atque corrupti quos dolores et quasatque corrupti quos dolores et quas occaecati cupie non provident</p>
    <div class="who"><span class="avatar"></span><div><b>Marcus Feld</b><span>United States</span></div></div>
  </div>
  <div class="abs tst" style="left:1088px;top:50px;width:280px">
    <div class="stars">★★</div>
    <p>At vero eos et accusamus et iusto odio dignissimos ducimus qui blaiis praesentium voluptatum deleniti atque corrupti quos dolores et occaecati cupie non provident</p>
    <div class="who"><span class="avatar"></span><div><b>Marcus Feld</b><span>United States</span></div></div>
  </div>
</div>

<footer class="abs footer">
  <svg width="1200" height="584" viewBox="0 0 1200 584">
    <polygon points="0,200 600,50 1200,200 1200,584 0,584" fill="#e0a82e"/>
    <polygon points="0,215 600,105 1200,215 1200,584 0,584" fill="#000"/>
    <circle cx="600" cy="68" r="42" fill="#fff"/>
    <circle cx="600" cy="68" r="14" fill="none" stroke="#e0a82e" stroke-width="2"/>
  </svg>
</footer>
<div class="abs f-brand">
  <span class="dot"></span>
  <div class="brand-name">BRAMBLETON</div>
  <div class="brand-sub">HOME SERVICES</div>
  <div class="tagline">Where Home Maintenance is Effortless</div>
</div>
<div class="abs f-col" style="left:451px">
  <h4>QUICK LINKS</h4>
  <ul><li>Home</li><li>About</li><li>Services</li><li>Testimonials</li><li>Contact Us</li></ul>
</div>
<div class="abs f-col" style="left:667px">
  <h4>HELP LINKS</h4>
  <ul><li>FAQ</li><li>Terms of use</li><li>Privacy Policy</li><li>Support Links</li><li>Conditions</li></ul>
</div>
<div class="abs f-contact">
  <h4>CONTACT US</h4>
  <div class="c-row"><span class="c-ic"><svg width="16" height="16" viewBox="0 0 24 24"><path d="M12 2a7 7 0 0 0-7 7c0 5 7 13 7 13s7-8 7-13a7 7 0 0 0-7-7zm0 9.5A2.5 2.5 0 1 1 12 6a2.5 2.5 0 0 1 0 5.5z" fill="#000"/></svg></span><span>Brambleton Homes<br>United States</span></div>
  <div class="c-row"><span class="c-ic"><svg width="16" height="16" viewBox="0 0 24 24"><path d="M6.6 10.8a15 15 0 0 0 6.6 6.6l2.2-2.2c.3-.3.7-.4 1-.2 1.1.4 2.3.6 3.6.6.6 0 1 .4 1 1V20c0 .6-.4 1-1 1A17 17 0 0 1 3 4c0-.6.4-1 1-1h3.5c.6 0 1 .4 1 1 0 1.3.2 2.5.6 3.6.1.3 0 .7-.2 1z" fill="#000"/></svg></span><span>+1 555 014 2290</span></div>
  <div class="c-row"><span class="c-ic"><svg width="16" height="16" viewBox="0 0 24 24"><path d="M3 5h18v14H3zm2 2v.5l7 4.5 7-4.5V7z" fill="#000"/></svg></span><span>hello@brambletonhomes.example</span></div>
</div>
<div class="abs rule"></div>
<div class="abs copy">Copyrights@2025.Brambleton Homes.All Rights Reserved</div>

</body>
</html>
```